Travel Blogger Business Card for roamquill.net

I need a two-sided business card for a travel blogging website. The card should be both professional and fun at the same time. This is for the website www.roamquill.net

I don't necessarily think that the current logo on the website needs to be used on the business card but it can be. I am very flexible with ideas

Target Market(s)

Travel agencies that will be met at a conference.

Industry/Entity Type

Travel

Contact Information for Business Card

Company Name: Roam Quill.net
Name: Bertrand Olesky
Voice: +1-(345)-402-7731
Address: Coral Reach Shore, Grand Cayman, Cayman Islands
Email: ceo@roamquill.net

Colors
0592cd
0355a3
3176b5
33a6d7
85cae6
85acd3

Requirements
Must have
• Website address and name should be bigger than address, phone number, and email.

```html
<!DOCTYPE html>
<html lang="en">
<head>
<meta charset="utf-8">
<title>Roam Quill business card</title>
<link rel="stylesheet" href="https://fonts.googleapis.com/css2?family=Open+Sans:wght@300;400;600;800&display=swap">
<style>
  :root {
    --sky: #85cae6;
    --line: #33a6d7;
    --deep: #0355a3;
    --mid: #3176b5;
    --white: #ffffff;
    --grey: #8a8f94;
    --page: #e2e2e2;
  }
  * { margin: 0; padding: 0; box-sizing: border-box; }
  html, body {
    width: 1200px; height: 1200px; overflow: hidden;
    background: var(--page);
    font-family: "Open Sans", sans-serif;
  }
  .sheet {
    width: 1200px; height: 1200px;
    display: flex; flex-direction: column; align-items: center; justify-content: center;
    gap: 56px;
  }
  .card {
    position: relative;
    width: 900px; height: 514px;
    background: var(--sky);
    box-shadow: 0 10px 30px rgba(0,0,0,0.12);
    overflow: hidden;
  }
  .card-frame {
    position: absolute; inset: 18px;
    border: 1.5px solid var(--white);
    pointer-events: none;
  }

  /* Front */
  .front-mark {
    position: absolute; left: 190px; top: 110px;
    width: 150px; height: 150px;
    background: var(--white);
  }
  .brand-name {
    position: absolute; left: 370px; top: 230px;
    font-weight: 800; font-size: 64px; letter-spacing: 1px;
    color: var(--white); text-transform: uppercase;
    line-height: 1;
  }
  .holder-name {
    position: absolute; left: 440px; top: 330px;
    font-weight: 300; font-size: 40px;
    color: var(--white);
  }

  /* Back */
  .back-pattern {
    position: absolute; inset: 0;
    background: linear-gradient(135deg, #85cae6 0%, #7cc3e2 50%, #85cae6 100%);
  }
  .contact-panel {
    position: absolute; left: 215px; top: 140px;
    width: 470px; height: 234px;
    background: var(--white);
    display: flex; flex-direction: column; justify-content: center; align-items: center;
    gap: 14px;
  }
  .contact-row {
    display: flex; align-items: flex-start; gap: 10px;
    color: var(--mid); font-weight: 600; font-size: 19px; line-height: 1.3;
  }
  .contact-row svg { flex: none; margin-top: 4px; }
  .contact-address { text-align: center; }
</style>
</head>
<body>
<main class="sheet">
  <section class="card card-front" aria-label="Business card front">
    <div class="card-frame"></div>
    <div class="front-mark"></div>
    <div class="brand-name">Roam Quill</div>
    <div class="holder-name">Bertrand Olesky</div>
  </section>

  <section class="card card-back" aria-label="Business card back">
    <div class="back-pattern" role="img" aria-label="Thin blue geometric line pattern radiating across light blue background"></div>
    <div class="card-frame"></div>
    <div class="contact-panel">
      <div class="contact-row">
        <svg width="14" height="16" viewBox="0 0 14 16" aria-hidden="true"><path d="M3 1 L6 1 L7 5 L5 6.5 Q6.5 10 9 11 L10.5 9 L13 10 L13 13 Q12 15 9 14.5 Q2 12 1 4 Q1 2 3 1 Z" fill="var(--grey)"/></svg>
        <span>+1-(345)-402-7731</span>
      </div>
      <div class="contact-row">
        <svg width="18" height="14" viewBox="0 0 18 14" aria-hidden="true"><rect x="1" y="1" width="16" height="12" fill="var(--grey)"/><path d="M1 1 L9 8 L17 1" stroke="var(--white)" stroke-width="1.5" fill="none"/></svg>
        <span>ceo@roamquill.net</span>
      </div>
      <div class="contact-row">
        <svg width="12" height="17" viewBox="0 0 12 17" aria-hidden="true"><path d="M6 16 Q0 8 0 6 A6 6 0 0 1 12 6 Q12 8 6 16 Z" fill="var(--grey)"/><circle cx="6" cy="6" r="2.2" fill="var(--white)"/></svg>
        <span class="contact-address">Coral Reach Shore,<br>Grand Cayman, Cayman Islands</span>
      </div>
    </div>
  </section>
</main>
</body>
</html>
```